Yoga Studio Postcard Advertising Flyer

Need a postcard size flyer that will promote our business. The objective is to promote location and availability. Want it to be personal. The objective to connect the audience to the purpose of yoga and the focus on enabling functional well-being. Something that is a very big focus at this point in time in the world. I really want people to see the value in connecting with us via our website, calmora app, pagewell or vibro. The colours are to be bright but not overwhelming and aligned to the logo colours. Its also important to have the location picture on the flyer - unless you think that it is way too much (try a with or without). I don't want this to be a specials brochure - it is an introduction to our brand and our business. No need to over do it with promotional lines apart from come and join us.

Delayed in organising this.

Local yogis and residence who are or want to be focused on well-being.

• Pictures - would have the logo on one side.
• Modern and aligned to website design.

```html
<!DOCTYPE html>
<html lang="en">
<head>
<meta charset="utf-8">
<title>Harbourlight Studio – Postcard</title>
<link rel="stylesheet" href="https://fonts.googleapis.com/css2?family=Jost:wght@300;400;600;700&family=Mrs+Saint+Delafield&display=swap">
<style>
  :root {
    --sky: #3a9ad9;
    --navy: #1c2240;
    --ink: #3a3d45;
    --bg-edge: #c5d8e7;
    --bg-mid: #eaf1f8;
    --photo-light: #d6d6d6;
    --photo-dark: #5a5a5a;
  }
  * { margin: 0; padding: 0; box-sizing: border-box; }
  html, body { width: 846px; height: 1200px; overflow: hidden; }
  body { font-family: "Jost", sans-serif; }

  .postcard {
    position: relative;
    width: 846px;
    height: 1200px;
    background: radial-gradient(ellipse at 55% 45%, var(--bg-mid) 0%, #dde8f2 55%, var(--bg-edge) 100%);
    overflow: hidden;
  }

  .website {
    position: absolute; left: 72px; top: 66px;
    font-weight: 700; font-size: 28px; color: var(--sky); letter-spacing: 0.2px;
  }
  .socials {
    position: absolute; left: 72px; top: 120px;
    display: flex; align-items: center; gap: 18px;
    font-size: 22px; font-weight: 300; color: var(--ink);
  }
  .socials .channel {
    font-size: 16px; font-weight: 600; color: var(--sky);
    display: flex; align-items: center; gap: 5px;
  }
  .socials .channel::before {
    content: ""; width: 10px; height: 10px; border-radius: 50%; background: var(--sky);
  }

  .brand {
    position: absolute; left: 576px; top: 80px; width: 224px;
    display: flex; flex-direction: column; align-items: center; gap: 12px;
  }
  .brand-dot { width: 46px; height: 46px; border-radius: 50%; background: var(--sky); }
  .brand-name {
    font-weight: 600; font-size: 24px; color: var(--navy); line-height: 1.1; white-space: nowrap;
  }

  .photo { position: absolute; left: 72px; width: 218px; }
  .photo-studio { top: 217px; height: 262px; background: linear-gradient(180deg, #eeeeee 0%, #cfcfcf 55%, var(--photo-dark) 100%); }
  .photo-teacher { top: 489px; height: 191px; background: linear-gradient(180deg, #e4e4e4 0%, #b9b9b9 60%, #7a7a7a 100%); }
  .photo-venue { top: 689px; height: 262px; background: linear-gradient(180deg, #e8e8e8 0%, var(--photo-light) 45%, #6d6d6d 100%); }

  .headline {
    position: absolute; left: 196px; top: 262px;
    font-family: "Mrs Saint Delafield", cursive; color: var(--navy);
    font-size: 100px; line-height: 0.85; font-weight: 400; white-space: nowrap;
  }
  .headline .line-two { display: block; padding-left: 276px; font-size: 108px; }

  .timeline { position: absolute; left: 0; top: 0; width: 846px; height: 1200px; }

  .value {
    position: absolute; left: 364px; width: 440px;
    font-size: 29px; line-height: 32px; color: var(--ink); font-weight: 300;
  }
  .value-1 { top: 503px; }
  .value-2 { top: 596px; }
  .value-3 { top: 721px; }

  .address {
    position: absolute; left: 364px; top: 902px;
    font-size: 23px; line-height: 28px; font-weight: 300; color: var(--sky);
  }

  .vision {
    position: absolute; left: 0; top: 1000px; width: 846px; text-align: center;
    font-weight: 700; font-size: 23.5px; line-height: 29px; color: var(--navy); letter-spacing: 1.5px;
  }

  .invite {
    position: absolute; left: 72px; top: 1072px; width: 707px;
    display: flex; align-items: center; gap: 26px;
  }
  .invite .rule { flex: 1; height: 2px; background: var(--sky); }
  .invite .call {
    font-family: "Mrs Saint Delafield", cursive; color: var(--sky);
    font-size: 92px; line-height: 1; white-space: nowrap;
  }
</style>
</head>
<body>
<main class="postcard">
  <div class="website">www.harbourlightstudio.com.au</div>
  <div class="socials">
    <span>Or find us on</span>
    <span class="channel">calmora</span>
    <span class="channel">pagewell</span>
    <span class="channel">chirpline</span>
    <span class="channel">vibro</span>
  </div>

  <div class="brand">
    <span class="brand-dot"></span>
    <span class="brand-name">Harbourlight Studio</span>
  </div>

  <div class="photo photo-studio" role="img" aria-label="Black and white photo of the studio interior with yoga mats and blocks laid out in a bright hall"></div>
  <div class="photo photo-teacher" role="img" aria-label="Black and white portrait of the yoga teacher by the sea"></div>
  <div class="photo photo-venue" role="img" aria-label="Black and white photo of the studio building, a small stone chapel behind a fence"></div>

  <h1 class="headline">Enable functional<span class="line-two">wellbeing</span></h1>

  <svg class="timeline" viewBox="0 0 846 1200" aria-hidden="true">
    <g stroke="#3a9ad9" stroke-width="1.6">
      <line x1="321" y1="378" x2="321" y2="512"/>
      <line x1="321" y1="556" x2="321" y2="622"/>
      <line x1="321" y1="666" x2="321" y2="748"/>
      <line x1="321" y1="792" x2="321" y2="902"/>
    </g>
    <g fill="#3a9ad9">
      <circle cx="321" cy="534" r="9"/>
      <circle cx="321" cy="644" r="9"/>
      <circle cx="321" cy="770" r="9"/>
      <path d="M320 913a14 14 0 0 0-14 14c0 10 14 25 14 25s14-15 14-25a14 14 0 0 0-14-14zm0 8a6 6 0 1 1 0 12a6 6 0 0 1 0-12z" fill-rule="evenodd"/>
    </g>
  </svg>

  <p class="value value-1">Strengthen your well-being<br>through adaptive yoga.</p>
  <p class="value value-2">Seek to evolve your mind and<br>body through the challenge<br>of yoga.</p>
  <p class="value value-3">Perfection is a desire and never<br>an outcome through the practice<br>of yoga.</p>

  <p class="address">The Chapel, 212 Harbour Road Eastlake,<br>NSW 2099</p>

  <p class="vision">Our vision is to create an atmosphere that enables<br>inclusiveness of the whole community.</p>

  <div class="invite">
    <span class="rule"></span>
    <span class="call">Come join us</span>
    <span class="rule"></span>
  </div>
</main>
</body>
</html>
```